Create Brisk Lesson Studio a card design that will stick in the mind of prospects.

Brisk Lesson Studio specialises designs and produces training video, animation, illustration and text.

We need a card design that oozes class and leaves the prospect brimming with confidence.

The design will feature the Brisk Lesson Studio all black logo (uploaded). The design may also use the shade of orange from the orange version of the logo (uploaded). Note, just the color is to be used e.g. for the back of the card, not the orange logo itself.

The Brisk brand is about authenticity, quality, maturity and assurance. We are a safe buy when it comes to the prospects next project.

Target Market(s)

The primary target is training managers or others who are responsible for choosing to hire companies to produce their training media e.g. video. This will usually be a large spend so they need to have confidence.

Industry/Entity Type

Training

Contact Information for Business Card

FRONT:

Brisk Lesson Studio
Phone: 03 5172 4039
1st Floor, 418 Kellerby Road
Mt Ferncombe
VIC 3862
Australia
www.brisklesson.com.au

Lionel Petch
Founder and Lead Consultant
mobile: +61 3 0462 735 218
email: lionel@brisklesson.com.au

BACK:
Specialising in design and production of training:

video
animation
illustration
text

for delivery via internet, intranet and/or LMS.

Number of Pages Required

4 page

Font styles to use
Sans Serif

Requirements
Must have
• The black logo uploaded with the brief.
Nice to have
• The inclusion of the shade of orange found in the orange logo also uploaded with the brief. One example would be having the back of the card in this orange and using a white font for the text. But I want the designer to work this out.
Should not have
• No colours other than black and the orange included in the uploaded orange logo.

```html
<!DOCTYPE html>
<html lang="en">
<head>
<meta charset="utf-8">
<title>Brisk Lesson Studio – Business Card</title>
<link rel="stylesheet" href="https://fonts.googleapis.com/css2?family=Source+Sans+3:wght@400;600;700&display=swap">
<style>
  :root {
    --orange: #f15a24;
    --grey: #939598;
    --ink: #3a3a3a;
    --black: #1a1a1a;
    --white: #ffffff;
    --backdrop: #3a3a3a;
  }
  * { margin: 0; padding: 0; box-sizing: border-box; }
  html, body { width: 1200px; height: 1200px; overflow: hidden; }
  body {
    background: var(--backdrop);
    font-family: "Source Sans 3", sans-serif;
    position: relative;
  }
  .card {
    position: absolute;
    left: 238px;
    width: 724px;
    height: 412px;
    background: var(--white);
    overflow: hidden;
  }
  .card--front { top: 154px; }
  .card--back { top: 635px; }

  .wave { position: absolute; inset: 0; width: 100%; height: 100%; }

  .name-marker {
    position: absolute; left: 0; top: 111px;
    width: 14px; height: 49px; background: var(--orange);
  }
  .person { position: absolute; left: 38px; top: 112px; }
  .person__name {
    color: var(--orange); font-weight: 700; font-size: 27px; line-height: 1.1;
  }
  .person__role { color: var(--ink); font-size: 19px; margin-top: 3px; }

  .contacts {
    position: absolute; left: 38px; top: 196px; list-style: none;
  }
  .contacts li {
    display: flex; align-items: center; gap: 8px;
    color: var(--ink); font-size: 19px; line-height: 24.5px;
  }
  .contacts svg { width: 17px; height: 17px; flex: none; }

  .brand-name {
    position: absolute; font-weight: 700; white-space: nowrap;
  }
  .brand-name--front {
    color: var(--orange); font-size: 34px; right: 41px; top: 88px;
  }

  .address {
    position: absolute; right: 41px; top: 258px;
    text-align: right; color: var(--white); font-size: 19px; line-height: 24.2px;
  }

  .back-content {
    position: absolute; inset: 0; text-align: center;
  }
  .brand-name--back {
    color: var(--black); font-size: 46px; left: 0; right: 0; top: 128px;
  }
  .services-intro {
    position: absolute; left: 0; right: 0; top: 280px;
    color: var(--black); font-size: 19.5px;
  }
  .services {
    position: absolute; left: 0; right: 0; top: 305px;
    font-size: 22px; color: var(--orange);
  }
  .services .sep { color: var(--black); margin: 0 3px; }
  .delivery {
    position: absolute; left: 0; right: 0; top: 351px;
    color: var(--black); font-size: 19px;
  }
</style>
</head>
<body>

<section class="card card--front" aria-label="Card front">
  <svg class="wave" viewBox="0 0 724 412" preserveAspectRatio="none" aria-hidden="true">
    <path d="M0,322 C180,342 380,300 540,228 C400,292 200,350 0,350 Z" fill="var(--grey)"/>
    <path d="M0,358 C200,372 410,312 560,248 C620,226 680,218 724,218 L724,412 L0,412 Z" fill="var(--orange)"/>
  </svg>

  <div class="name-marker"></div>
  <div class="person">
    <p class="person__name">Lionel Petch</p>
    <p class="person__role">Founder and Lead Consultant</p>
  </div>

  <ul class="contacts">
    <li>
      <svg viewBox="0 0 16 16"><rect x="4" y="1" width="8" height="14" rx="1.5" fill="none" stroke="var(--orange)" stroke-width="1.5"/><circle cx="8" cy="12.5" r="0.9" fill="var(--orange)"/></svg>
      +61 3 0462 735 218
    </li>
    <li>
      <svg viewBox="0 0 16 16"><path d="M1,6 C1,2 15,2 15,6 L12,7 L11,5 C9,4.5 7,4.5 5,5 L4,7 Z" fill="var(--orange)"/><path d="M4,8 L12,8 L14,14 L2,14 Z" fill="var(--orange)"/><circle cx="8" cy="11" r="1.6" fill="var(--white)"/></svg>
      Phone: 03 5172 4039
    </li>
    <li>
      <svg viewBox="0 0 16 16"><rect x="1" y="3.5" width="14" height="9" fill="var(--orange)"/><path d="M1,3.5 L8,9 L15,3.5" fill="none" stroke="var(--white)" stroke-width="1.2"/></svg>
      lionel@brisklesson.com.au
    </li>
    <li>
      <svg viewBox="0 0 16 16" fill="none" stroke="var(--orange)" stroke-width="1.2"><circle cx="8" cy="8" r="6.5"/><ellipse cx="8" cy="8" rx="3" ry="6.5"/><path d="M1.5,8 H14.5 M2.5,4.8 H13.5 M2.5,11.2 H13.5"/></svg>
      www.brisklesson.com.au
    </li>
  </ul>

  <p class="brand-name brand-name--front">Brisk Lesson Studio</p>

  <address class="address" style="font-style:normal">
    Brisk Lesson Studio<br>
    1st Floor, 418 Kellerby Road<br>
    Mt Ferncombe<br>
    VIC 3862<br>
    Australia
  </address>
</section>

<section class="card card--back" aria-label="Card back">
  <div class="back-content">
    <p class="brand-name brand-name--back">Brisk Lesson Studio</p>
    <p class="services-intro">Specialising in design and production of training</p>
    <p class="services">video<span class="sep">|</span>animation<span class="sep">|</span>illustration<span class="sep">|</span>text</p>
    <p class="delivery">for delivery via internet, intranet and/or LMS.</p>
  </div>
</section>

</body>
</html>
```